Business Card Design

Comprehensive Wealth Management

We provide the following services:
Asset Protection
Trust Administration
Estate Planning - Wills & Trusts
Management of Assets, Stocks, Bonds, ETF's, and Mutual Funds
Tax Planning
Financial Planning
Multi-Generational Planning
Business Planning
Retirement Planning
Risk Management
Hi Designers, please see the attached link for a sample of our website that you can see what we do and you may or may not use the same colors and style. Be creative please.
http://danielforsythe.sitebrook.example/

Target Market(s)

Widows, Trust beneficiaries, Trustees, retirees and those getting ready for retirement

Industry/Entity Type

Business

Contact Information for Business Card

Law Offices of Daniel R. Forsythe
48217 Calloway Avenue, Suite 206
Woodland Hills, California 90000
p: 555.014.2296
f: 555.014.2297
e: dforsythe@meridianwx.example

Daniel R. Forsythe, Esq., CPA, CFP

Colors
0293ce
33a6d7
86cae7
0555a3
3377b5
85acd3
00a990
34b8a4
87d0c7

Requirements
Must have
• I would like a design that really pops. I have a sample brochure that has a molecular structure with the various topics on each molecule. I like the various shades of blue. I can send you the brochure sample if you like.
Nice to have
• Very high end design/logo of some kind that has a modern art look. We primarily work with high net worth and ultra high net worth clients. It should be unique looking. Maybe with pretty greens and blues.

```html
<!DOCTYPE html>
<html lang="en">
<head>
<meta charset="utf-8">
<title>Daniel R. Forsythe — Business Card</title>
<link rel="stylesheet" href="https://fonts.googleapis.com/css2?family=EB+Garamond:ital,wght@0,400;0,500;1,400&display=swap">
<style>
  :root {
    --page: #ffffff;
    --ink-dark: #221f1e;
    --ink-text: #2a2a2a;
    --gold: #a89a73;
    --panel-grey: #9a9a9a;
    --white: #ffffff;
    --card-edge: #c9c9c9;
  }
  * { margin: 0; padding: 0; box-sizing: border-box; }
  html, body {
    width: 1200px; height: 685px; overflow: hidden;
    background: var(--page);
    font-family: "EB Garamond", Georgia, serif;
  }
  .canvas { position: relative; width: 1200px; height: 685px; }

  .card { position: absolute; width: 478px; height: 274px; overflow: hidden; }
  .card--front { left: 57px; top: 186px; background: var(--ink-dark); }
  .card--back { left: 669px; top: 185px; background: var(--white); border: 1px solid var(--card-edge); }

  .wordmark {
    position: absolute; color: var(--white);
    font-weight: 400; letter-spacing: 0.5px; white-space: nowrap;
  }
  .card--front .wordmark { left: 0; right: 0; top: 104px; text-align: center; font-size: 40px; }
  .card--back .wordmark { left: 18px; top: 18px; font-size: 26px; color: var(--ink-dark); }

  .address-band {
    position: absolute; left: 0; right: 0; bottom: 0; height: 52px;
    background: var(--ink-dark);
    display: flex; align-items: center; padding-left: 28px;
    font-size: 14.5px; letter-spacing: 0.4px; white-space: nowrap; color: var(--white);
  }
  .card--front .address-band { bottom: 6px; }
  .address-band .soft { color: var(--gold); text-transform: uppercase; font-size: 12.5px; }
  .address-band .sep { color: var(--gold); margin: 0 6px; font-size: 12px; }

  .holder { position: absolute; left: 29px; top: 103px; font-size: 13.5px; color: var(--ink-text); }
  .contact { position: absolute; left: 29px; top: 142px; list-style: none; font-size: 12px; color: var(--ink-text); line-height: 16.5px; }
  .contact li:first-child { margin-bottom: 3px; }
  .contact .label { color: var(--gold); font-weight: 500; }

  .services {
    position: absolute; right: 0; top: 0; width: 196px; height: 213px;
    background: var(--panel-grey); padding: 16px 10px 0 27px;
    list-style: none; color: var(--white); font-style: italic;
    font-size: 11.6px; line-height: 16.5px;
  }
  .services li.tight { line-height: 12.8px; margin: 2px 0 2px; }
</style>
</head>
<body>
<main class="canvas">
  <section class="card card--front" aria-label="Business card front">
    <h1 class="wordmark">Daniel R. Forsythe</h1>
    <p class="address-band">48217&nbsp;<span class="soft">Calloway Avenue, Suite</span>&nbsp;206<span class="sep">|</span><span class="soft">Woodland Hills, CA</span>&nbsp;90000</p>
  </section>

  <section class="card card--back" aria-label="Business card back">
    <p class="wordmark">Daniel R. Forsythe</p>
    <p class="holder">Daniel R. Forsythe, Esq., CPA, CFP</p>
    <ul class="contact">
      <li><span class="label">E:</span> dforsythe@meridianwx.example</li>
      <li><span class="label">P:</span> 555.014.2296</li>
      <li><span class="label">F:</span> 555.014.2297</li>
    </ul>
    <ul class="services">
      <li>Asset Protection</li>
      <li>Trust Administration</li>
      <li>Estate Planning - Wills &amp; Trusts</li>
      <li class="tight">Management of Assets, Stocks, Bonds, ETF's, &amp; Mutual Funds</li>
      <li>Tax Planning</li>
      <li>Financial Planning</li>
      <li>Multi-Generational Planning</li>
      <li>Business Planning</li>
      <li>Retirement Planning</li>
      <li>Risk Management</li>
    </ul>
    <p class="address-band">48217&nbsp;<span class="soft">Calloway Avenue, Suite</span>&nbsp;206<span class="sep">|</span><span class="soft">Woodland Hills, CA</span>&nbsp;90000</p>
  </section>
</main>
</body>
</html>
```